Cover design for new academic journal on deconstruction and psychoanalysis

We need a cover for a new academic journal on deconstruction and psychoanalysis. The name of the journal is "The Suspended Threshold: A Journal of Deconstruction and Psychoanalysis" (ST) and it is published by the Halvern College Press(HCP).

Here is a description of the journal on the HCP website:

http://www.halvernpress.example.edu/product/The-Suspended-Threshold,318264.aspx

We are looking for a design that is more abstract and does not have icons or photographs of people, especially not photos of Kovalt or Brisk. The design should be contemporary with clean lines and simple fonts. Again, it should be abstract, with no icons or iconography.

The cover should simply have the full name of the journal and then "Volume 1, Issue 1, 2014" on the cover and "Vol. 1, No. 1, 2014" on the spine.

Attached you can see some ideas that we rejected from HCP. It is important that you understand that these designs were rejected and are just being offered as examples of what the cover will look like in general, as a template of sorts.

The cover should have a bold abstract design, with a space for the title and "Volume 1, Issue 1, 2014."

Something bold and contemporary.

Target Market(s)

Academics, scholars and psychoanalysts.

Industry/Entity Type

University

Font styles to use
Sans Serif

Requirements
Must have
• Must be abstract, bold, have color, and must be contemporary.
Should not have
• No icons, no photographs of Kovalt, Brisk, or anyone.

```html
<!DOCTYPE html>
<html lang="en">
<head>
<meta charset="utf-8">
<title>The Suspended Threshold — Journal Cover</title>
<link rel="stylesheet" href="https://fonts.googleapis.com/css2?family=PT+Sans&display=swap">
<style>
  :root {
    --ink: #031614;
    --spine: #061e1c;
    --teal-text: #3fd8cd;
    --teal-bar: #3b8c88;
    --art-bright: #3fb5aa;
    --art-light: #2a8c84;
    --art-mid: #14514c;
    --art-dark: #061f1d;
    --art-rose: rgba(240, 196, 184, 0.75);
    --art-plum: rgba(150, 60, 110, 0.55);
  }
  html, body {
    margin: 0;
    padding: 0;
    overflow: hidden;
    background: var(--ink);
  }
  .cover {
    position: relative;
    width: 1200px;
    height: 844px;
    background: var(--ink);
    font-family: "PT Sans", "Myriad Pro", sans-serif;
    color: var(--teal-text);
    overflow: hidden;
  }
  .band {
    position: absolute;
    background: var(--teal-bar);
  }
  .band--back-top { left: 8px; top: 227px; width: 582px; height: 13px; }
  .band--front-top { left: 629px; top: 227px; width: 566px; height: 13px; }
  .band--base { left: 4px; top: 712px; width: 1192px; height: 4px; }

  .artwork {
    position: absolute;
    top: 240px;
    height: 472px;
  }
  .artwork--back {
    left: 0;
    width: 592px;
    background:
      radial-gradient(ellipse 22% 34% at 40% 40%, var(--art-rose), transparent 75%),
      radial-gradient(ellipse 20% 26% at 52% 66%, var(--art-plum), transparent 75%),
      radial-gradient(ellipse 55% 62% at 62% 50%, var(--art-bright), var(--art-light) 30%, var(--art-mid) 62%, var(--art-dark) 100%);
  }
  .artwork--front {
    left: 627px;
    width: 573px;
    background:
      radial-gradient(ellipse 22% 34% at 58% 40%, var(--art-rose), transparent 75%),
      radial-gradient(ellipse 20% 26% at 46% 66%, var(--art-plum), transparent 75%),
      radial-gradient(ellipse 55% 62% at 36% 50%, var(--art-bright), var(--art-light) 30%, var(--art-mid) 62%, var(--art-dark) 100%);
  }

  .spine {
    position: absolute;
    left: 592px;
    top: 90px;
    width: 35px;
    height: 626px;
    background: var(--spine);
  }
  .spine__title,
  .spine__issue {
    position: absolute;
    left: 2px;
    writing-mode: vertical-rl;
    font-size: 24px;
    line-height: 30px;
    white-space: nowrap;
  }
  .spine__title { top: 6px; }
  .spine__issue { top: 456px; font-size: 22px; }

  .masthead {
    position: absolute;
    right: 73px;
    top: 40px;
    text-align: right;
  }
  .masthead__title {
    margin: 0;
    font-weight: 400;
    font-size: 40px;
    line-height: 50px;
  }
  .masthead__issue {
    margin: 6px 0 0;
    font-size: 18px;
  }
  .tagline {
    position: absolute;
    right: 73px;
    top: 730px;
    margin: 0;
    text-align: right;
    font-size: 25px;
    line-height: 32px;
  }
</style>
</head>
<body>
<main class="cover">
  <div class="band band--back-top"></div>
  <div class="band band--front-top"></div>

  <div class="artwork artwork--back" role="img" aria-label="Bold abstract teal illustration with bursts of radiating lines and a pale rose, veined arching form"></div>
  <div class="artwork artwork--front" role="img" aria-label="Mirrored bold abstract teal illustration with bursts of radiating lines and a pale rose, veined arching form"></div>

  <div class="band band--base"></div>

  <aside class="spine">
    <span class="spine__title">The Suspended Threshold</span>
    <span class="spine__issue">Vol. 1, No. 1, 2014</span>
  </aside>

  <header class="masthead">
    <h1 class="masthead__title">The<br>Suspended<br>Threshold</h1>
    <p class="masthead__issue">volume 1 issue 1 2014</p>
  </header>

  <p class="tagline">A journal of deconstruction<br>and psychoanalysis</p>
</main>
</body>
</html>
```